BriskLoom Wordpress Website

We require a WordPress website that emulates the sleek design and functionality of https://www.tulvorix.example and https://quenlap.example/. The site should showcase our AI-powered customer support solutions with a modern, professional aesthetic.
Homepage
The homepage should feature a bold headline highlighting our AI capabilities, followed by concise sections outlining our key offerings:
AI-powered customer support
Data integration and deployment
Knowledge system integration
AI help desks and chat agents
Customer feedback insights
Include eye-catching visuals or animations to illustrate these concepts.
Navigation
The main navigation menu should include:
Product
Platform
Company
News
Learn More
Key Pages
Product Page: Detail our AI solutions, their benefits, and use cases.
Platform Page: Explain our technology, integration capabilities, and deployment process.
Company Page: Share our mission, team, and values.
News Page: Feature latest updates, press releases, and blog posts.
Call-to-Action
Implement a prominent "Learn More" button that directs users to an enrollment page. Our team will manage inquiries from this point.
Footer
Include a "Contact Us" section in the footer for easy access to our contact information.
Design Elements
Use a clean, minimalist design with ample white space
Incorporate a color scheme that reflects trust and innovation
Utilize smooth scrolling and subtle animations for enhanced user experience
Ensure mobile responsiveness for all devices
Technical Requirements
Build on WordPress for easy content management
Optimize for fast loading speeds and SEO
The website should convey our expertise in AI-driven customer support solutions while providing an intuitive user experience that guides visitors toward learning more about our services
Industry/Entity Type
AI Chat Agents

```html
<!DOCTYPE html>
<html lang="en">
<head>
<meta charset="utf-8">
<title>BriskLoom — AI Conversational Platform</title>
<link href="https://fonts.googleapis.com/css2?family=Outfit:wght@300;400;500;600&display=swap" rel="stylesheet">
<style>
:root{
  --ink:#121717;
  --muted:#3d4646;
  --teal-dark:#2c5f5e;
  --teal:#3f8b8a;
  --teal-soft:#e3eeee;
  --panel:#eff2f3;
  --card:#eef3f3;
  --line:#d7dddd;
  --white:#ffffff;
}
*{box-sizing:border-box;margin:0;padding:0}
html,body{width:1200px;height:3597px;overflow:hidden;background:var(--white)}
body{font-family:'Outfit',sans-serif;color:var(--ink);position:relative}
.abs{position:absolute}
.btn{position:absolute;display:flex;align-items:center;justify-content:center;background:var(--teal-dark);color:var(--white);font-size:13px;font-weight:500;border-radius:8px;text-decoration:none;box-shadow:0 6px 12px rgba(44,95,94,.25)}
.photo{position:absolute;overflow:hidden}
.brand{display:flex;align-items:center;gap:10px;color:var(--teal-dark);font-weight:400}
.brand-dot{border-radius:50%;background:var(--teal-dark)}
/* nav */
.nav-links{position:absolute;left:439px;top:27px;display:flex;gap:21px;font-size:13px;font-weight:500}
/* hero */
.eyebrow{left:0;width:1200px;top:142px;text-align:center;font-size:14px;color:var(--teal)}
.hero-title{left:0;width:1200px;top:170px;text-align:center;font-size:42px;font-weight:600;line-height:53px}
.hero-note{left:141px;top:381px;width:190px;font-size:14px;line-height:22px}
.stat{position:absolute;left:876px;display:flex;align-items:center;gap:17px;font-size:17px;font-weight:500}
.stat-icon{width:56px;height:56px;border-radius:12px;background:var(--teal-soft);display:flex;align-items:center;justify-content:center}
.section-title{left:0;width:1200px;text-align:center;font-size:31px;font-weight:500;line-height:41px}
/* offer cards */
.offer{position:absolute;top:836px;width:289px;height:199px;background:var(--card);border-radius:12px;padding:25px}
.offer-icon{width:56px;height:56px;border-radius:10px;background:var(--teal-dark);display:flex;align-items:center;justify-content:center;box-shadow:0 6px 10px rgba(44,95,94,.25)}
.offer h3{font-size:18px;font-weight:500;margin-top:23px}
.offer p{font-size:13px;line-height:21px;margin-top:9px;color:var(--muted)}
/* enable */
.h2{font-size:31px;font-weight:500;line-height:40px}
.body-sm{font-size:13px;line-height:22px;color:var(--muted)}
/* trust */
.panel{position:absolute;left:141px;width:916px;background:var(--panel);border-radius:24px}
.checks{list-style:none}
.checks li{display:flex;align-items:center;gap:10px;font-size:15px;height:30px}
/* features */
.feature{position:absolute;top:2119px;width:213px;height:212px;background:var(--teal);border-radius:10px;color:var(--white);text-align:center;padding-top:22px}
.feature h3{font-size:15px;font-weight:500;margin-top:10px}
.feature p{font-size:13px;line-height:21px;margin:6px 16px 0;opacity:.92}
.feature .arrow{margin-top:6px}
/* footer */
.foot-col h4{font-size:17px;font-weight:500;color:var(--teal)}
.foot-col ul{list-style:none;margin-top:17px}
.foot-col li{font-size:13px;height:27.4px}
.contact-row{display:flex;gap:10px;align-items:flex-start;font-size:13px;line-height:17px}
.social{position:absolute;top:3552px;width:25px;height:25px;border-radius:50%;background:var(--teal-dark)}
</style>
</head>
<body>

<!-- header -->
<header>
  <div class="abs brand" style="left:141px;top:12px;font-size:31px">
    <span class="brand-dot" style="width:46px;height:46px"></span>BriskLoom
  </div>
  <nav class="nav-links">
    <span>Home</span><span>Product</span><span>Platform</span><span>Company</span><span>News</span><span>Learn More</span><span>Key Pages</span>
  </nav>
  <a class="btn" style="left:946px;top:15px;width:111px;height:39px">Contact Us</a>
</header>

<!-- hero -->
<div class="abs" style="left:64px;top:204px;width:115px;height:125px;border-radius:50%;background:#eef2f2"></div>
<p class="abs eyebrow">Meet BriskLoom</p>
<h1 class="abs hero-title">Elevate Your Users' Experience, A New<br>Type Of Conversation Awaits.</h1>
<a class="btn" style="left:543px;top:304px;width:113px;height:39px">Get Started</a>
<p class="abs hero-note">Enhance your customer experience with BriskLoom's AI Assistant.</p>
<div class="photo" role="img" aria-label="Photo of a person relaxing on a sofa with a laptop" style="left:141px;top:469px;width:174px;height:85px;border-radius:43px;background:linear-gradient(135deg,#6b7a86,#c49060 60%,#3e4a55)"></div>
<div class="photo" role="img" aria-label="Photo of a man with headphones working on a laptop in a café" style="left:357px;top:361px;width:484px;height:263px;border-radius:20px;background:linear-gradient(120deg,#5a4236,#a88a72 45%,#d9d2c8 70%,#6d6a55)"></div>
<div class="abs" style="left:520px;top:345px;width:160px;height:30px;background:var(--white);border-radius:0 0 22px 22px"></div>
<div class="stat" style="top:416px">
  <span class="stat-icon"><svg width="30" height="30" viewBox="0 0 30 30" fill="none" stroke="#3f8b8a" stroke-width="1.8"><circle cx="15" cy="15" r="11" stroke-dasharray="5 2"/><path d="M10 15l3.5 3.5L20 11"/></svg></span>Always Ready
</div>
<div class="abs" style="left:876px;top:492px;width:202px;height:1px;background:var(--line)"></div>
<div class="stat" style="top:515px">
  <span class="stat-icon"><svg width="32" height="32" viewBox="0 0 32 32" fill="none" stroke="#3f8b8a" stroke-width="1.6"><circle cx="16" cy="16" r="12" stroke-dasharray="4 2"/><text x="16" y="19.5" text-anchor="middle" font-size="9" font-family="Outfit,sans-serif" fill="#3f8b8a" stroke="none">24/7</text></svg></span>Always on - 24/7
</div>

<!-- offers -->
<h2 class="abs section-title" style="top:717px">Revolutionize Your<br>Customer Interactions</h2>
<div class="offer" style="left:141px">
  <div class="offer-icon"><svg width="30" height="30" viewBox="0 0 30 30" fill="none" stroke="#fff" stroke-width="1.6"><rect x="4" y="7" width="15" height="12" rx="2"/><path d="M8 19v4l4-4"/><circle cx="20" cy="10" r="6"/><path d="M18.5 8.5a1.5 1.5 0 1 1 1.5 2v1"/></svg></div>
  <h3>Get Answers</h3>
  <p>Users will find the information they need in seconds</p>
</div>
<div class="offer" style="left:455px">
  <div class="offer-icon"><svg width="30" height="30" viewBox="0 0 30 30" fill="none" stroke="#fff" stroke-width="1.6"><path d="M11 16a6 6 0 1 1 8 0v3h-8z"/><path d="M12 22h6"/><path d="M15 2v2M6 6l1.5 1.5M24 6l-1.5 1.5"/><path d="M4 25c3-2 6-2 9 0h8"/></svg></div>
  <h3>Solve Problems</h3>
  <p>Concerns will be addressed quickly with expert assistance</p>
</div>
<div class="offer" style="left:769px">
  <div class="offer-icon"><svg width="30" height="30" viewBox="0 0 30 30" fill="none" stroke="#fff" stroke-width="1.6"><path d="M10 20c2-8 7-13 15-15-2 8-7 13-15 15z"/><circle cx="18" cy="12" r="2"/><path d="M10 20l-3-1 3-5M10 20l1 3 5-3M5 25l4-4"/></svg></div>
  <h3>Take Action</h3>
  <p>Users will activate services and features immediately</p>
</div>

<!-- enables -->
<div class="photo" role="img" aria-label="Photo of a humanoid robot beside a man using a laptop" style="left:141px;top:1129px;width:328px;height:297px;border-radius:0 16px 0 16px;background:linear-gradient(120deg,#8a5a44,#d8cfc4 40%,#c9b49b 65%,#5b3a2a)"></div>
<h2 class="abs h2" style="left:554px;top:1150px">BriskLoom Enables You To</h2>
<p class="abs body-sm" style="left:554px;top:1208px">Engage and delight customers with an AI agent aligned to your brand<br>Provide real-time support for a wide variety of uses from simple to complex</p>
<h3 class="abs" style="left:554px;top:1276px;font-size:16px;font-weight:500">Make AI Your Own With BriskLoom's Conversational Platform</h3>
<p class="abs body-sm" style="left:554px;top:1312px">Ground your BriskLoom AI agent in your company's identity and knowledge<br>Solve problems quickly and effectively</p>
<div class="photo" role="img" aria-label="Photo of a robot and a man working at computers" style="left:841px;top:1378px;width:216px;height:104px;border-radius:52px;background:linear-gradient(120deg,#2d3a4a,#6b8aa8 45%,#3b4654)"></div>

<!-- trust -->
<section class="panel" style="top:1568px;height:384px">
  <h2 class="abs h2" style="left:74px;top:45px;line-height:40px">BriskLoom Prioritizes Trust<br>And Security</h2>
  <ul class="abs checks" style="left:72px;top:137px">
    <li><svg width="18" height="18" viewBox="0 0 18 18"><circle cx="9" cy="9" r="9" fill="#2c5f5e"/><path d="M5 9.2l2.6 2.6L13 6.5" fill="none" stroke="#fff" stroke-width="1.8"/></svg>Built-in supervision and auditing</li>
    <li><svg width="18" height="18" viewBox="0 0 18 18"><circle cx="9" cy="9" r="9" fill="#2c5f5e"/><path d="M5 9.2l2.6 2.6L13 6.5" fill="none" stroke="#fff" stroke-width="1.8"/></svg>Secure integrations</li>
    <li><svg width="18" height="18" viewBox="0 0 18 18"><circle cx="9" cy="9" r="9" fill="#2c5f5e"/><path d="M5 9.2l2.6 2.6L13 6.5" fill="none" stroke="#fff" stroke-width="1.8"/></svg>Strong data governance and privacy</li>
  </ul>
  <p class="abs" style="left:72px;top:240px;font-size:13px;line-height:21px">Discover how BriskLoom can transform your customer experience<br>with customized conversational AI</p>
  <a class="btn" style="left:72px;top:301px;width:151px;height:39px">Contact Us Today</a>
  <div class="photo" role="img" aria-label="Illustration of an AI figure with a security shield beside a woman at a computer" style="left:544px;top:28px;width:345px;height:328px;border-radius:0 14px 0 14px;background:linear-gradient(120deg,#0f2340,#2d6fb0 40%,#13294a 70%,#3a4a66)"></div>
</section>

<!-- features -->
<h2 class="abs section-title" style="top:2038px">Key Features</h2>
<div class="feature" style="left:141px">
  <svg width="60" height="44" viewBox="0 0 60 44" fill="none" stroke="#fff" stroke-width="1.6"><rect x="2" y="2" width="56" height="34" rx="3"/><path d="M24 12l-6 7 6 7M36 12l6 7-6 7M32 10l-4 18"/><path d="M0 40h60"/></svg>
  <h3>No-Code Agent Creation</h3>
  <p>Build custom AI agents in minutes using our intuitive interface</p>
  <svg class="arrow" width="22" height="12" viewBox="0 0 22 12" fill="none" stroke="#fff" stroke-width="1.4"><path d="M1 6h19M15 1l5 5-5 5"/></svg>
</div>
<div class="feature" style="left:375px">
  <svg width="44" height="44" viewBox="0 0 44 44" fill="none" stroke="#fff" stroke-width="1.6"><path d="M12 28a10 10 0 1 1 20 0"/><circle cx="22" cy="20" r="5"/><path d="M22 28v8M16 40h12M22 8V4M10 14l-3-2M34 14l3-2"/></svg>
  <h3>Powerful Orchestration</h3>
  <p>Coordinate complex, multi-step workflows across systems</p>
  <svg class="arrow" width="22" height="12" viewBox="0 0 22 12" fill="none" stroke="#fff" stroke-width="1.4"><path d="M1 6h19M15 1l5 5-5 5"/></svg>
</div>
<div class="feature" style="left:610px">
  <svg width="44" height="44" viewBox="0 0 44 44" fill="none" stroke="#fff" stroke-width="1.6"><path d="M20 6a18 18 0 1 0 18 18H20z"/><path d="M25 2v17h17A17 17 0 0 0 25 2z"/><path d="M30 8l6 6M28 13l6 4"/></svg>
  <h3>Comprehensive Analytics</h3>
  <p>Gain actionable insights from customer interactions</p>
  <svg class="arrow" width="22" height="12" viewBox="0 0 22 12" fill="none" stroke="#fff" stroke-width="1.4"><path d="M1 6h19M15 1l5 5-5 5"/></svg>
</div>
<div class="feature" style="left:844px">
  <svg width="56" height="44" viewBox="0 0 56 44" fill="none" stroke="#fff" stroke-width="1.6"><path d="M16 30a8 8 0 0 1 2-16 11 11 0 0 1 21 3 7 7 0 0 1-1 13z"/><path d="M28 30v8M18 14l-8-8M38 14l8-8M16 30l-8 6M40 30l8 6"/><circle cx="8" cy="4" r="2"/><circle cx="48" cy="4" r="2"/><circle cx="6" cy="38" r="2"/><circle cx="50" cy="38" r="2"/><circle cx="28" cy="40" r="2"/></svg>
  <h3>Seamless Integration</h3>
  <p>Our platform integrates natively with popular CRM and support tools</p>
  <svg class="arrow" width="22" height="12" viewBox="0 0 22 12" fill="none" stroke="#fff" stroke-width="1.4"><path d="M1 6h19M15 1l5 5-5 5"/></svg>
</div>
<a class="btn" style="left:526px;top:2374px;width:146px;height:39px">View All Features</a>

<!-- why -->
<div class="photo" role="img" aria-label="Illustration of a friendly chatbot beside a smiling woman using a laptop" style="left:141px;top:2500px;width:384px;height:269px;border-radius:0 16px 0 16px;background:linear-gradient(120deg,#bcd4e6,#eef0ef 45%,#d6c3ab 75%,#9aa5ac)"></div>
<h2 class="abs h2" style="left:604px;top:2530px">Why Choose BriskLoom?</h2>
<p class="abs body-sm" style="left:604px;top:2586px;width:430px;color:var(--ink)">Transform your customer experience with AI agents that are truly an extension of your brand, created effortlessly through our no-code platform. Request a demo today to see how BriskLoom can revolutionize your support and service operations in record time.</p>
<a class="btn" style="left:604px;top:2702px;width:110px;height:39px">Learn More</a>

<!-- discuss -->
<section class="panel" style="top:2856px;height:259px">
  <h2 class="abs" style="left:0;width:916px;top:55px;text-align:center;font-size:31px;font-weight:500">Let's Discuss How We Can Help You</h2>
  <p class="abs" style="left:0;width:916px;top:120px;text-align:center;font-size:13px;color:var(--muted)">Learn how BriskLoom can improve your customer interactions at a lower cost</p>
  <a class="btn" style="left:383px;top:164px;width:150px;height:39px">Contact Us Today</a>
  <svg class="abs" style="left:590px;top:130px" width="170" height="130" viewBox="0 0 170 130" fill="none" stroke="#6b7878" stroke-width="1.2">
    <path d="M130 30c-20 25-60 0-80 20-12 12-14 28 4 30 18 2 16-20-4-18-20 2-26 25-22 48" stroke-dasharray="4 4"/>
    <path d="M135 20l30-14-12 32-8-10z M145 28l20-22"/>
  </svg>
</section>

<!-- footer -->
<footer>
  <div class="abs" style="left:1020px;top:3340px;width:180px;height:195px;border-radius:50%;background:#f2f5f5"></div>
  <div class="abs brand" style="left:141px;top:3324px;font-size:52px">
    <span class="brand-dot" style="width:82px;height:82px"></span>BriskLoom
  </div>
  <div class="abs foot-col" style="left:513px;top:3256px">
    <h4>Quick Links</h4>
    <ul><li>Home</li><li>Product</li><li>Platform</li><li>Company</li><li>News</li><li>Learn More</li><li>Key Pages</li></ul>
  </div>
  <div class="abs foot-col" style="left:692px;top:3256px">
    <h4>Resources</h4>
    <ul><li>Privacy Policy</li><li>Terms Of Service</li><li>Contact</li></ul>
  </div>
  <div class="abs foot-col" style="left:876px;top:3256px">
    <h4>Contact Info</h4>
    <div class="contact-row" style="margin-top:17px"><svg width="16" height="18" viewBox="0 0 16 18" fill="#2c5f5e"><path d="M8 0a6 6 0 0 0-6 6c0 4.5 6 10 6 10s6-5.5 6-10a6 6 0 0 0-6-6zm0 8.5A2.5 2.5 0 1 1 8 3.5a2.5 2.5 0 0 1 0 5z"/><rect x="2" y="16.5" width="12" height="1.5"/></svg><span>123 Lorem Ipsum Dummy,<br>#567 Dummy Road 1234</span></div>
    <div class="contact-row" style="margin-top:15px"><svg width="16" height="13" viewBox="0 0 16 13" fill="#2c5f5e"><rect width="16" height="13" rx="2"/><path d="M1 2l7 5 7-5" fill="none" stroke="#fff" stroke-width="1.4"/></svg><span>info@briskloom.example</span></div>
    <div class="contact-row" style="margin-top:17px"><svg width="15" height="15" viewBox="0 0 15 15" fill="#2c5f5e"><path d="M3 0l3 3-1.5 2.5a9 9 0 0 0 5 5L12 9l3 3-2 3C6 15 0 9 0 2z"/></svg><span>123-456-7890</span></div>
  </div>
  <div class="abs" style="left:141px;top:3539px;width:916px;height:1px;background:var(--line)"></div>
  <p class="abs" style="left:141px;top:3557px;font-size:13px">© Copyright 2024 BriskLoom. All Rights Reserved.</p>
  <span class="social" style="left:927px"></span>
  <span class="social" style="left:961px"></span>
  <span class="social" style="left:996px"></span>
  <span class="social" style="left:1032px"></span>
</footer>

</body>
</html>
```